What makes us Different Managed Communications Services Provider Flyer

We need a flyer to explain why we are different than other "managed IT services" company. Gives a brief description of our company and services that can entice clients and potential clients to setup a FREE consultation with us. This will become part of an ongoing marketing campaign that includes emails, leave behinds, brochures, and more

```html
<!DOCTYPE html>
<html lang="en">
<head>
<meta charset="utf-8">
<title>Keystone Comms – Flyer</title>
<link href="https://fonts.googleapis.com/css2?family=Bebas+Neue&family=Montserrat:wght@400;500;600;700&display=swap" rel="stylesheet">
<style>
  :root{
    --stage:#525252;
    --blue:#0a4ea3;
    --blue-deep:#0a3f8f;
    --cyan:#3bbcd4;
    --cyan-light:#5fd0e3;
    --ink:#4a4a4a;
    --ink-dark:#3a3a3a;
    --paper:#ffffff;
    --panel:#eeeeee;
  }
  *{box-sizing:border-box;margin:0;padding:0}
  html,body{width:1200px;height:1117px;overflow:hidden;background:var(--stage)}
  body{position:relative;font-family:"Montserrat",sans-serif;color:var(--ink)}
  .page{position:absolute;top:214px;width:533px;height:688px;background:var(--paper);overflow:hidden;box-shadow:0 14px 30px rgba(0,0,0,.35)}
  .page--front{left:59px}
  .page--back{left:608px}
  .abs{position:absolute}
  .art{position:absolute;left:0;top:0}

  /* front */
  .brand{position:absolute;left:44px;top:112px;display:flex;align-items:center;gap:8px;font-weight:700;font-size:19px;color:var(--blue);white-space:nowrap}
  .brand__mark{width:13px;height:13px;background:var(--cyan)}
  .hero-title{position:absolute;left:40px;top:198px;font-family:"Bebas Neue",sans-serif;color:#fff;font-size:55px;line-height:51px;letter-spacing:.3px}
  .hero-sub{position:absolute;left:40px;top:305px;font-family:"Bebas Neue",sans-serif;color:var(--cyan-light);font-size:36px;line-height:36px}
  .body{font-size:10.1px;line-height:13.3px;color:var(--ink)}
  .hl{color:var(--cyan);font-weight:700}
  .intro-left{left:41px;top:386px;width:212px}
  .intro-right{left:278px;top:386px;width:222px}
  .panel-grey{position:absolute;left:0;top:547px;width:533px;height:141px;background:var(--panel)}
  .commit{left:41px;top:557px;width:456px}
  .site{position:absolute;left:153px;top:649px;width:227px;height:39px;background:var(--blue);border-radius:12px 12px 0 0;display:flex;align-items:center;justify-content:center;gap:10px;color:#fff;font-weight:700;font-size:13px}
  .site__dot{width:10px;height:10px;border-radius:50%;border:2px solid var(--cyan)}

  /* section tabs */
  .tab{position:absolute;left:0;width:533px;height:36px}
  .tab__label{position:absolute;top:6px;display:flex;align-items:center;gap:9px;font-family:"Bebas Neue",sans-serif;color:#fff;font-size:22px;line-height:24px;white-space:nowrap}
  .tab__mark{width:9px;height:9px;background:#fff;flex:0 0 9px}

  /* back */
  .holistic-title{position:absolute;left:45px;top:34px;display:flex;gap:9px;font-family:"Bebas Neue",sans-serif;color:#fff;font-size:24px;line-height:21px}
  .holistic-title .tab__mark{margin-top:6px}
  .holistic-text{position:absolute;left:45px;top:93px;width:262px;color:#fff;font-size:9.8px;line-height:13.3px;font-weight:600}
  .services{position:absolute;left:21px;top:166px;width:491px;height:134px;background:#efefef;border-radius:6px;border-bottom:5px solid var(--cyan);display:grid;grid-template-columns:1fr 1fr;padding:14px 16px 0 24px;column-gap:16px;row-gap:10px}
  .service{display:flex;gap:14px;align-items:flex-start}
  .service__icon{flex:0 0 30px;height:34px}
  .service__text{font-size:9.8px;line-height:12.7px;font-weight:600;color:var(--ink-dark);max-width:165px}
  .deliver{left:45px;top:360px;width:440px}
  .deliver p+p{margin-top:13px}
  .rule{position:absolute;left:45px;width:438px;height:1px;background:var(--cyan)}
  .trust{left:45px;top:554px;width:440px}
  .closing{position:absolute;left:45px;top:622px;width:443px;height:66px;background:var(--blue);border-radius:12px 12px 0 0;color:#fff;font-weight:700;font-size:9.6px;line-height:13.3px;text-align:center;padding:14px 20px 0}
</style>
</head>
<body>

<!-- Front page -->
<section class="page page--front">
  <svg class="art" width="533" height="380" viewBox="0 0 533 380">
    <defs>
      <linearGradient id="frontHeader" x1="0" y1="0" x2="0" y2="1">
        <stop offset="0" stop-color="#3bbcd4"/>
        <stop offset=".18" stop-color="#0a55ad"/>
        <stop offset="1" stop-color="#0a4ea3"/>
      </linearGradient>
      <linearGradient id="frontStripe" x1="0" y1="0" x2="0" y2="1">
        <stop offset="0" stop-color="#0a4ea3"/>
        <stop offset="1" stop-color="#3bbcd4"/>
      </linearGradient>
      <linearGradient id="frontPhoto" x1="0" y1="0" x2="1" y2="1">
        <stop offset="0" stop-color="#8a8d91"/>
        <stop offset=".6" stop-color="#3c3a3a"/>
        <stop offset="1" stop-color="#1c1b1c"/>
      </linearGradient>
    </defs>
    <polygon points="199,0 533,0 533,290 305,191" fill="url(#frontPhoto)" role="img" aria-label="Photo of a support agent wearing a headset"/>
    <polygon points="183,0 199,0 305,191 289,191" fill="url(#frontStripe)"/>
    <path d="M0,326 L330,362 C370,362 380,330 420,330 L533,330 L533,346 L430,346 C395,346 380,372 335,372 L0,372 Z" fill="#e4e4e4"/>
    <path d="M0,191 L400,191 C455,191 495,235 533,268 L533,320 L420,320 C385,320 375,356 330,356 L0,356 Z" fill="url(#frontHeader)"/>
  </svg>
  <div class="brand"><span class="brand__mark"></span>Keystone Comms</div>

  <h1 class="hero-title">More than just<br>A managed IT provider</h1>
  <h2 class="hero-sub">Our legacy of excellence</h2>

  <p class="abs body intro-left">At our company, we are far more than your typical managed IT provider. Since our founding in 1983, we have built a reputation based on trust, reliability, and unparalleled service. With <span class="hl">client relationships spanning 20 to 30 years,</span> we have demonstrated a level of commitment that few IT firms can match.</p>
  <p class="abs body intro-right">What sets us apart is not just our technical expertise but the <span class="hl">deep, long-term partnerships</span> we cultivate with our clients—many of whom have stayed with us <span class="hl">without ever being locked into a contract.</span> That is a testament to the exceptional quality of our service and the trust we have earned over decades.</p>

  <div class="panel-grey"></div>
  <div class="tab" style="top:507px">
    <svg class="art" width="533" height="36" viewBox="0 0 533 36">
      <path d="M16,35 L32,4 Q34,0 40,0 L305,0 Q311,0 315,4 L336,31 L425,31 L425,35 Z" fill="var(--cyan)"/>
      <rect x="430" y="30" width="103" height="5" fill="var(--blue)"/>
    </svg>
    <div class="tab__label" style="left:42px"><span class="tab__mark"></span>A commitment beyond contracts</div>
  </div>
  <p class="abs body commit">Unlike many managed IT providers who rely on rigid contracts to retain clients, we believe that service excellence speaks for itself. The longevity of our client relationships is rooted in our ability to <span class="hl">anticipate needs, resolve challenges before they escalate, and proactively enhance network &amp; communication infrastructures.</span> Our <span class="hl">comprehensive checklists, questionnaires, policies, and procedures, attention to details ensure that every client receives a tailored, best-in-class experience from day one.</span></p>
  <div class="site"><span class="site__dot"></span>www.keystonecomms.com</div>
</section>

<!-- Back page -->
<section class="page page--back">
  <svg class="art" width="533" height="250" viewBox="0 0 533 250">
    <defs>
      <linearGradient id="backHeader" x1="0" y1="0" x2="0" y2="1">
        <stop offset="0" stop-color="#3bbcd4"/>
        <stop offset=".12" stop-color="#0a55ad"/>
        <stop offset="1" stop-color="#0a4ea3"/>
      </linearGradient>
      <linearGradient id="backStripe" x1="0" y1="0" x2="0" y2="1">
        <stop offset="0" stop-color="#0a4ea3"/>
        <stop offset="1" stop-color="#3bbcd4"/>
      </linearGradient>
      <linearGradient id="backPhoto" x1="0" y1="0" x2="1" y2="1">
        <stop offset="0" stop-color="#c9cdd1"/>
        <stop offset=".55" stop-color="#e7e9ea"/>
        <stop offset="1" stop-color="#6d9cc6"/>
      </linearGradient>
    </defs>
    <polygon points="255,0 533,0 533,244 396,244" fill="url(#backPhoto)" role="img" aria-label="Photo of a smiling support agent with a headset at a computer"/>
    <polygon points="0,0 245,0 378,229 0,229" fill="url(#backHeader)"/>
    <polygon points="245,0 257,0 396,244 384,244" fill="url(#backStripe)"/>
  </svg>
  <h2 class="holistic-title"><span class="tab__mark"></span><span>A holistic approach<br>to IT management</span></h2>
  <p class="holistic-text">We don't just manage IT—we integrate ourselves into your business, ensuring that technology aligns with your strategic goals. Our services go beyond traditional break-fix support; we offer:</p>

  <div class="services">
    <div class="service">
      <svg class="service__icon" viewBox="0 0 30 34"><polygon points="15,0 30,8.5 30,25.5 15,34 0,25.5 0,8.5" fill="var(--blue)"/><polyline points="8,22 13,16 17,19 23,12" fill="none" stroke="#fff" stroke-width="1.8"/><polyline points="19,12 23,12 23,16" fill="none" stroke="#fff" stroke-width="1.8"/></svg>
      <p class="service__text">Strategic IT Roadmaps customized to drive business growth.</p>
    </div>
    <div class="service">
      <svg class="service__icon" viewBox="0 0 30 34"><polygon points="15,0 30,8.5 30,25.5 15,34 0,25.5 0,8.5" fill="var(--blue)"/><circle cx="15" cy="17" r="6" fill="none" stroke="#fff" stroke-width="1.6"/><circle cx="15" cy="17" r="2" fill="#fff"/></svg>
      <p class="service__text">Comprehensive backup and disaster recovery solutions that provide peace of mind.</p>
    </div>
    <div class="service">
      <svg class="service__icon" viewBox="0 0 30 34"><polygon points="15,0 30,8.5 30,25.5 15,34 0,25.5 0,8.5" fill="var(--blue)"/><path d="M15,8 L22,11 L22,17 Q22,23 15,26 Q8,23 8,17 L8,11 Z" fill="none" stroke="#fff" stroke-width="1.6"/><polyline points="11.5,17 14,19.5 18.5,14.5" fill="none" stroke="#fff" stroke-width="1.6"/></svg>
      <p class="service__text">Proactive cybersecurity assessments that help keep businesses secure.</p>
    </div>
    <div class="service">
      <svg class="service__icon" viewBox="0 0 30 34"><polygon points="15,0 30,8.5 30,25.5 15,34 0,25.5 0,8.5" fill="var(--blue)"/><path d="M9,12 Q8,15 11,20 Q15,25 19,25 L21,23 L18,20 L16,21 Q13,19 12,16 L13,14 L11,11 Z" fill="#fff"/><circle cx="19" cy="12" r="3.5" fill="none" stroke="#fff" stroke-width="1.3"/></svg>
      <p class="service__text">Industry-leading response times and dedicated support teams focused on delivering an exceptional client experience.</p>
    </div>
  </div>

  <div class="tab" style="top:317px">
    <svg class="art" width="533" height="36" viewBox="0 0 533 36">
      <path d="M16,35 L32,4 Q34,0 40,0 L330,0 Q336,0 340,4 L361,31 L448,31 L448,35 Z" fill="var(--cyan)"/>
      <rect x="453" y="30" width="80" height="5" fill="var(--blue)"/>
    </svg>
    <div class="tab__label" style="left:45px"><span class="tab__mark"></span>Our clients stay because we deliver</div>
  </div>
  <div class="abs body deliver">
    <p>For over 40 years, we have maintained a standard of excellence that <span class="hl">other companies simply cannot compare with.</span> Our team of experts consistently goes above and beyond, ensuring that clients not only <span class="hl">get the support they need but also receive the strategic guidance necessary to stay ahead in an ever-evolving digital landscape.</span></p>
    <p>Our <span class="hl">90-day performance review</span> process ensures that we continuously improve our service based on client feedback. This process allows us to <span class="hl">adapt, refine, and enhance our approach,</span> providing a truly personalized IT experience that aligns with business objectives.</p>
  </div>
  <div class="rule" style="top:492px"></div>

  <div class="tab" style="top:509px">
    <svg class="art" width="533" height="36" viewBox="0 0 533 36">
      <path d="M16,35 L32,4 Q34,0 40,0 L300,0 Q306,0 310,4 L331,31 L419,31 L419,35 Z" fill="var(--cyan)"/>
      <rect x="424" y="30" width="109" height="5" fill="var(--blue)"/>
    </svg>
    <div class="tab__label" style="left:45px"><span class="tab__mark"></span>A legacy of trust &amp; reliability</div>
  </div>
  <p class="abs body trust">The fact that many of our clients have remained with us for <span class="hl">decades without a formal contract</span> speaks volumes about the trust we have built. We don't lock in clients with paperwork—we keep them with results. <span class="hl">That's the difference between a standard managed IT provider and an IT partner who genuinely cares.</span></p>
  <div class="closing">If you're looking for an IT provider that will treat your business as if it were their own, look no further. Our legacy of service, innovation, and commitment to our clients is what sets us apart from the rest.</div>
</section>

</body>
</html>
```